" Trabalhei muitos anos em escritórios de Arquitetura, Construtoras, Escritórios de projetos para grandes Magazines, tive uma sociedade onde fiz obras e projetos de decoração, mas agora finalmente estou criando a Movera para trabalhar como autônoma. Vou juntar toda minha experiência nesses anos e aplicar na realização dos sonhos dos clientes. "

```html
<!DOCTYPE html>
<html lang="pt-BR">
<head>
<meta charset="utf-8">
<title>Movera – Papel timbrado</title>
<link href="https://fonts.googleapis.com/css2?family=Montserrat:wght@300;400&display=swap" rel="stylesheet">
<style>
  :root {
    --backdrop: #e4e4e4;
    --paper: #ffffff;
    --copper: #c6906f;
    --band: #edcdb8;
    --band-ink: #8f7565;
    --watermark: #ececec;
  }
  * { margin: 0; padding: 0; box-sizing: border-box; }
  html, body { width: 1200px; height: 1200px; overflow: hidden; background: var(--backdrop); }
  body { font-family: "Montserrat", sans-serif; position: relative; }

  .letterhead {
    position: absolute; left: 220px; top: 60px;
    width: 760px; height: 1080px;
    background: var(--paper);
    box-shadow: 0 2px 10px rgba(0,0,0,0.08);
  }
  .brand {
    position: absolute; top: 70px; left: 0; right: 0;
    text-align: center; color: var(--copper);
  }
  .brand-mark {
    width: 44px; height: 44px; border-radius: 50%;
    background: var(--copper); margin: 0 auto 10px;
  }
  .brand-name {
    font-weight: 300; font-size: 64px; letter-spacing: 6px; line-height: 1;
    text-transform: uppercase;
  }
  .brand-tagline {
    font-weight: 400; font-size: 11px; letter-spacing: 5px; margin-top: 8px;
    text-transform: uppercase;
  }
  .watermark {
    position: absolute; top: 390px; left: 0; right: 0;
    text-align: center; font-weight: 300; font-size: 150px;
    letter-spacing: 8px; color: var(--watermark); text-transform: uppercase;
  }
  .footer-band {
    position: absolute; left: 0; right: 0; bottom: 0; height: 170px;
    background: var(--band);
    padding: 26px 40px 0 40px;
    color: var(--band-ink); font-size: 13px;
  }
  .contact-list { list-style: none; }
  .contact-list li { display: flex; align-items: center; gap: 10px; height: 38px; }
  .contact-icon { width: 22px; height: 22px; flex: none; }
  .location {
    position: absolute; right: 40px; bottom: 44px;
    letter-spacing: 5px; font-size: 12px; text-transform: uppercase;
  }
</style>
</head>
<body>
  <main class="letterhead">
    <header class="brand">
      <div class="brand-mark"></div>
      <div class="brand-name">Movera</div>
      <div class="brand-tagline">Arquitetura | Interiores</div>
    </header>

    <div class="watermark" aria-hidden="true">Movera</div>

    <footer class="footer-band">
      <ul class="contact-list">
        <li>
          <svg class="contact-icon" viewBox="0 0 22 22" aria-hidden="true">
            <circle cx="11" cy="11" r="10" fill="none" stroke="currentColor" stroke-width="1.3"/>
            <path d="M7.5 6.5c.6-.6 1.4-.5 1.7.1l.9 1.7c.2.5 0 1-.4 1.3l-.5.4c.6 1.3 1.6 2.3 2.9 2.9l.4-.5c.3-.4.8-.6 1.3-.4l1.7.9c.6.3.7 1.1.1 1.7-1 1-2.6 1-4.3-.1-1.5-1-2.7-2.2-3.7-3.7-1.1-1.7-1.1-3.3-.1-4.3z" fill="currentColor"/>
          </svg>
          <span>(21) 98765-4321</span>
        </li>
        <li>
          <svg class="contact-icon" viewBox="0 0 22 22" aria-hidden="true">
            <circle cx="11" cy="11" r="10" fill="none" stroke="currentColor" stroke-width="1.3"/>
            <rect x="6" y="7.5" width="10" height="7" fill="none" stroke="currentColor" stroke-width="1.2"/>
            <path d="M6 7.5l5 4 5-4" fill="none" stroke="currentColor" stroke-width="1.2"/>
          </svg>
          <span>contato@movera.arq.br</span>
        </li>
        <li>
          <svg class="contact-icon" viewBox="0 0 22 22" aria-hidden="true">
            <circle cx="11" cy="11" r="10" fill="none" stroke="currentColor" stroke-width="1.3"/>
          </svg>
          <span>instagram.com/moveraarquitetura</span>
        </li>
      </ul>
      <div class="location">Rio de Janeiro - RJ | Brasil</div>
    </footer>
  </main>
</body>
</html>
```